Wine Label Redesign For California Wine Company

We’re looking to refresh our brand with a new professional looking label. We love what we have and was well received over the past three years and would like to keep a couple of the element: Name (Hugo Brantley), it doesn’t have to be in cursive. The swirl, this how everybody recognizes our brand as it’s also in our logo. Colors: Gold and whatever you think is awesome. Looking forward to seeing your work.

Target Market(s)

Retailers

Industry/Entity Type

Winery

Font styles to use
Serif
Script

Colors

Designer to choose colors to be used in the design.

Requirements
Must have
• Front Label:
• Symphony (Varietal)
• 2016 (vintage)
• Lodi, California (location)
• Hugo Brantley (Name)
• Back Label:
• Government Warning
• www.brantleywineco.com (website)
• 2016 (vintage)
• Swirl
Nice to have
• Creativity
• Bold colors
• Something that pops
Should not have
• Should not look nothing like my old label.

```html
<!DOCTYPE html>
<html lang="en">
<head>
<meta charset="utf-8">
<title>Symphony – Hugo Brantley Wine Label</title>
<link rel="stylesheet" href="https://fonts.googleapis.com/css2?family=Bebas+Neue&display=swap">
<style>
  :root {
    --page: #ffffff;
    --ink: #333333;
    --ink-text: #222222;
    --white: #ffffff;
    --teal: #1f6585;
    --green: #27b14a;
    --leaf: #5dbe4e;
    --lime: #9acb55;
    --mustard: #dfd95a;
    --lemon: #fdee66;
  }
  html, body {
    margin: 0;
    padding: 0;
    width: 940px;
    height: 1200px;
    overflow: hidden;
    background: var(--page);
  }
  .label {
    display: block;
    width: 940px;
    height: 1200px;
  }
  .label-type {
    font-family: "Bebas Neue", "Oswald", sans-serif;
  }
  .varietal { fill: var(--white); font-size: 118px; }
  .producer { fill: var(--white); font-size: 50px; letter-spacing: 4px; }
  .vintage { fill: var(--ink-text); font-size: 64px; }
  .origin { fill: var(--ink-text); font-size: 52px; letter-spacing: 4px; }
</style>
</head>
<body>
<svg class="label" viewBox="0 0 940 1200" xmlns="http://www.w3.org/2000/svg" aria-label="Symphony 2016 wine label by Hugo Brantley, Lodi, California">
  <defs>
    <linearGradient id="sky-fade" x1="0" y1="73" x2="0" y2="1140" gradientUnits="userSpaceOnUse">
      <stop offset="0" stop-color="var(--teal)"/>
      <stop offset="0.2" stop-color="var(--green)"/>
      <stop offset="0.38" stop-color="var(--lime)"/>
      <stop offset="0.5" stop-color="var(--mustard)"/>
      <stop offset="0.8" stop-color="var(--lemon)"/>
      <stop offset="1" stop-color="var(--lemon)"/>
    </linearGradient>
    <linearGradient id="field-fade" x1="65" y1="0" x2="876" y2="0" gradientUnits="userSpaceOnUse">
      <stop offset="0.06" stop-color="var(--green)"/>
      <stop offset="0.27" stop-color="var(--mustard)"/>
      <stop offset="0.45" stop-color="var(--lemon)"/>
      <stop offset="1" stop-color="var(--lemon)"/>
    </linearGradient>
    <filter id="fold-shadow" x="-10%" y="-10%" width="120%" height="130%">
      <feDropShadow dx="0" dy="8" stdDeviation="7" flood-color="#000" flood-opacity="0.35"/>
    </filter>
  </defs>

  <!-- Label ground -->
  <rect class="label-ground" x="65" y="73" width="811" height="1067" fill="url(#field-fade)"/>
  <polygon class="label-upper" points="65,73 876,73 876,905 65,522" fill="url(#sky-fade)" filter="url(#fold-shadow)"/>

  <!-- Crossing rails -->
  <g class="rails" stroke="var(--ink)" stroke-width="11" fill="none">
    <line x1="86" y1="1010" x2="590" y2="775"/>
    <line x1="86" y1="1045" x2="625" y2="792"/>
    <line x1="86" y1="507" x2="854" y2="864"/>
    <line x1="86" y1="537" x2="854" y2="892"/>
  </g>

  <!-- Frame -->
  <rect class="frame" x="86" y="94" width="768" height="1026" fill="none" stroke="var(--ink)" stroke-width="12"/>

  <!-- Title block -->
  <g class="title-block">
    <rect x="142" y="216" width="657" height="230" fill="var(--ink)"/>
    <rect class="vintage-panel" x="156" y="231" width="152" height="202" fill="var(--leaf)"/>
    <rect class="producer-band" x="323" y="367" width="463" height="66" fill="var(--leaf)"/>
    <text class="label-type vintage" x="226" y="364" text-anchor="middle">MMXVI</text>
    <text class="label-type varietal" x="555" y="328" text-anchor="middle">SYMPHONY</text>
    <text class="label-type producer" x="554" y="418" text-anchor="middle">HUGO BRANTLEY</text>
  </g>

  <text class="label-type origin" x="836" y="1095" text-anchor="end">LODI, CALIFORNIA</text>
</svg>
</body>
</html>
```